Lawn & Garden Maintenace Business card design needed

I need a basic business card design for a Lawn Mowing & Garden Maintenance business

I would like it to look a combination of classy, striking, with vibrant Green/s, I will attached a very rough idea of what I would like but I am open to new suggestions, and the possibility of doing it on a darker charcoal or black gloss card, please don't just send me a version of what I've attached it's a very rough idea & more based around the text layout than anything else, feel free to let your creative instincts fly!

Must have grass across the bottom of the Card & i would prefer it to be portrait rather than landscape.

I quite like the coloring of this previously submitted card
http://www.artspark-example.com/design/2840613

Please have the text in White and Green if you are submitting a dark card, thank you.

Business

R.K. Lawn & Garden Services

Free Quote - Great Rates

Rob Kessler
0417 362 918
Info@RKLawnAndGarden.example.au

Requirements
Must have
• Must have grass across bottom of card preferably photo real grass rather than illustrated.
Nice to have
• Small telephone icon for phone number small email icon for email address but only if both icon are similar size and don't take away from the overall look of the card

Would also be nice to a have a flow/style that would be easily transferable to flyers & advertising

```html
<!DOCTYPE html>
<html lang="en">
<head>
<meta charset="utf-8">
<title>R.K. Lawn &amp; Garden Services – Business Card</title>
<link rel="stylesheet" href="https://fonts.googleapis.com/css2?family=Arimo:wght@700&display=swap">
<style>
  :root {
    --backdrop: #2a2a2a;
    --card-black: #0b0b0b;
    --card-charcoal: #2b2b2b;
    --grass-deep: #1f6a12;
    --grass-bright: #3fae1f;
    --grass-light: #6fcf3a;
    --text-white: #ffffff;
    --text-soft: #e6e6e6;
  }
  * { box-sizing: border-box; margin: 0; padding: 0; }
  html, body {
    width: 1200px; height: 900px; overflow: hidden;
    background: var(--backdrop);
    font-family: "Arimo", Arial, sans-serif;
  }
  .canvas {
    width: 1200px; height: 900px;
    display: flex; align-items: center; justify-content: center;
  }
  .business-card {
    position: relative;
    width: 900px; height: 540px;
    overflow: hidden;
    background: linear-gradient(160deg, var(--card-charcoal) 0%, var(--card-black) 55%);
    box-shadow: 0 20px 50px rgba(0,0,0,.55);
  }
  .grass-field {
    position: absolute; left: 0; right: 0; bottom: 0; height: 330px;
    background:
      linear-gradient(to bottom, rgba(11,11,11,1) 0%, rgba(11,11,11,0) 45%),
      linear-gradient(to bottom, var(--grass-deep) 0%, var(--grass-bright) 55%, var(--grass-light) 100%);
  }
  .gloss {
    position: absolute; inset: 0;
    background: linear-gradient(115deg, rgba(255,255,255,0) 30%, rgba(255,255,255,.07) 30.2%, rgba(255,255,255,.04) 58%, rgba(255,255,255,0) 58.2%);
    pointer-events: none;
  }
  .brand-name {
    position: absolute; left: 64px; top: 74px;
    color: var(--text-white);
    font-weight: 700;
    text-transform: uppercase;
    line-height: .95;
    letter-spacing: -1px;
  }
  .brand-name span { display: block; }
  .brand-name .initials { font-size: 72px; }
  .brand-name .lawn { font-size: 72px; }
  .brand-name .garden { font-size: 46px; }
  .brand-name .services { font-size: 34px; letter-spacing: 1px; }
  .offer {
    position: absolute; left: 400px; top: 82px;
    color: var(--text-white);
    font-weight: 700; font-size: 30px; letter-spacing: 1.5px;
    text-transform: uppercase;
  }
  .offer .rates { display: block; margin-left: 22px; }
  .offer .divider {
    display: block; height: 0; width: 270px; margin: 10px 0 10px 10px;
    border-top: 2px dashed var(--text-white);
  }
  .contact {
    position: absolute; left: 460px; right: 0; top: 262px;
    color: var(--text-white);
    font-weight: 700; text-transform: uppercase;
  }
  .contact-row { display: flex; align-items: center; gap: 12px; }
  .contact-row::after {
    content: ""; flex: 1; border-top: 2px dashed var(--text-white); margin-right: 0;
  }
  .contact-name { font-size: 26px; letter-spacing: 1.5px; }
  .contact-phone { font-size: 18px; letter-spacing: 1px; margin-top: 8px; padding-left: 14px; color: var(--text-soft); }
  .contact-email {
    position: absolute; left: 290px; top: 408px;
    color: var(--text-white);
    font-weight: 700; font-size: 21px; letter-spacing: 1.5px;
    text-transform: uppercase;
  }
</style>
</head>
<body>
  <main class="canvas">
    <section class="business-card">
      <div class="grass-field" role="img" aria-label="Photo of lush green lawn grass across the bottom of the card"></div>
      <div class="gloss"></div>

      <h1 class="brand-name">
        <span class="initials">R.K.</span>
        <span class="lawn">Lawn</span>
        <span class="garden">&amp; Garden</span>
        <span class="services">Services</span>
      </h1>

      <p class="offer">
        Free Quote
        <span class="divider"></span>
        <span class="rates">Great Rates</span>
      </p>

      <div class="contact">
        <p class="contact-row contact-name">Rob Kessler</p>
        <p class="contact-row contact-phone">Ph: 0417 362 918</p>
      </div>

      <p class="contact-email">Info@RKLawnAndGarden.example.au</p>
    </section>
  </main>
</body>
</html>
```